Designs for a Barrister's chambers

Design stationery (including business card and letterhead) for a barrister's chambers -- similar to a law firm, using the enclosed logo. The current designs are not fit for purpose.

```html
<!DOCTYPE html>
<html lang="en">
<head>
<meta charset="utf-8">
<title>Lindale Chambers – Letterhead</title>
<link rel="stylesheet" href="https://fonts.googleapis.com/css2?family=Open+Sans:wght@400;600;700&display=swap">
<style>
  :root {
    --backdrop: #adadad;
    --paper: #ffffff;
    --navy: #131e33;
    --teal: #0b93b5;
    --ink-light: #ffffff;
  }
  * { margin: 0; padding: 0; box-sizing: border-box; }
  html, body {
    width: 1200px; height: 1200px; overflow: hidden;
    background: var(--backdrop);
    font-family: "Open Sans", Arial, sans-serif;
  }
  .letterhead {
    position: absolute; left: 204px; top: 41px;
    width: 792px; height: 1118px;
    background: var(--paper);
    overflow: hidden;
  }
  .letterhead__shapes { position: absolute; inset: 0; width: 100%; height: 100%; }
  .brand {
    position: absolute; left: 31px; top: 44px;
    display: flex; align-items: center; gap: 14px;
  }
  .brand__square { width: 64px; height: 64px; background: var(--teal); }
  .brand__name {
    color: var(--ink-light); font-weight: 600;
    font-size: 33px; line-height: 36px; letter-spacing: -0.3px;
  }
  .registration {
    position: absolute; right: 54px; top: 38px;
    color: var(--ink-light); font-weight: 700; font-size: 13.5px;
    letter-spacing: 0.3px; word-spacing: 2px;
  }
  .registration span + span { margin-left: 12px; }
  .company-line {
    position: absolute; right: 53px; top: 95px;
    color: var(--ink-light); font-weight: 700; font-size: 21px;
    letter-spacing: 1px;
  }
  .contact {
    position: absolute; top: 1035px;
    display: flex; align-items: center; gap: 10px;
    color: var(--ink-light); font-size: 12px; line-height: 16px;
    letter-spacing: 0.2px;
  }
  .contact svg { flex: none; }
  .contact--phone { left: 148px; }
  .contact--web { left: 306px; }
  .contact--address { left: 577px; }
</style>
</head>
<body>
  <main class="letterhead">
    <svg class="letterhead__shapes" viewBox="0 0 1013 1430" preserveAspectRatio="none" aria-hidden="true">
      <path class="header-band" fill="var(--navy)" d="M0 0 H1013 V120 H445 L382 192 Q375 199 362 199 H0 Z"/>
      <path class="header-ribbon" fill="var(--teal)" d="M488 88 H1013 V185 H390 L452 101 Q461 88 488 88 Z"/>
      <path class="footer-band" fill="var(--navy)" d="M148 1304 H1013 V1393 H79 Z"/>
    </svg>

    <div class="brand">
      <div class="brand__square"></div>
      <div class="brand__name">Lindale<br>Chambers</div>
    </div>

    <p class="registration"><span>VAT : 40981726</span><span>REG : 40981726</span></p>
    <p class="company-line">LINDALE CHAMBERS LIMITED</p>

    <div class="contact contact--phone">
      <svg width="26" height="36" viewBox="0 0 26 36" fill="none" stroke="#fff" stroke-width="2">
        <rect x="2" y="1" width="22" height="34" rx="3"/>
        <line x1="2" y1="6" x2="24" y2="6"/>
        <line x1="2" y1="29" x2="24" y2="29"/>
      </svg>
      <p>+0203 555 010<br>+0203 555 0102</p>
    </div>

    <div class="contact contact--web">
      <svg width="32" height="24" viewBox="0 0 32 24" fill="none" stroke="#fff" stroke-width="2">
        <rect x="1" y="1" width="30" height="22" rx="2"/>
        <path d="M1 3 L16 14 L31 3"/>
        <path d="M1 22 L12 11 M31 22 L20 11"/>
      </svg>
      <p>www.lindalechambers.com<br>clerks@lindalechambers.com</p>
    </div>

    <div class="contact contact--address">
      <svg width="28" height="38" viewBox="0 0 28 38" fill="none" stroke="#fff" stroke-width="2">
        <path d="M14 37 C6 26 2 20 2 14 A12 12 0 0 1 26 14 C26 20 22 26 14 37 Z"/>
        <circle cx="14" cy="14" r="5"/>
      </svg>
      <p>42 Carter Lane, London<br>EC4V 5AB</p>
    </div>
  </main>
</body>
</html>
```